Web design for Marketplace

Guys!
1st of all, thank you for willing to help me out.
I have attached PDF file with examples.
I am looking for professional and clean design for my new project “ Lantern of Seers “. Its marketplace for Psychic Readers around the world. Where they will able to register to provide their services via Chat,Email and sell their products on their personal stores.
Customer will able to get services and buy products from Psychic on Marketplace.
url : http://www.lanternofseers-demo.net
Please note: it doesn’t matter, what my current site looks like. I am looking for completely new design.
It doesn't matter if you add or remove : Clipvale video or even text which is on the home page in new design.
Following are the main pages of the website, which i am looking to be design.
1. Home page
2. Psychic
3. Marketplace
4. Psychic profile page
5. Psychic Store page
6. Psychic product page
7. Logo
following is the website, which i like the most. I would love to have something like that. It is neat , clean and friendly. I am looking for depth in design and neatness and borders (matter and a lot and it should be prefect ).
http://www.craftnook-demo.net
P.S : i believe it will be helpful to choose one of you. If you can only create design of " Homepage" at 1st , so i can go ahead and hire one of you guys.
Best,
Hi guys!
Guys,

```html
<!DOCTYPE html>
<html lang="en">
<head>
<meta charset="utf-8">
<title>Lantern of Seers – Home</title>
<link rel="stylesheet" href="https://fonts.googleapis.com/css2?family=Open+Sans:ital,wght@0,400;0,600;0,700;1,400;1,600&family=Archivo+Narrow:wght@700&display=swap">
<style>
:root{
  --orange:#f05a0e;
  --orange-soft:#f27b3c;
  --ink:#555;
  --text:#666;
  --dark:#111;
  --grey-band:#e6e6e6;
  --panel:#f1f1f1;
  --line:#d8d8d8;
  --blue:#1c8fd6;
  --social-grey:#d5d5d5;
}
*{box-sizing:border-box;margin:0;padding:0}
html,body{width:1200px;height:917px;overflow:hidden;background:#fff;font-family:"Open Sans",sans-serif;color:var(--text)}
.page{position:relative;width:1200px;height:917px}
.abs{position:absolute}

/* header */
.site-header{left:0;top:0;width:1200px;height:88px;background:linear-gradient(#3a3a3a,#0b0b0b)}
.brand{left:100px;top:0;width:272px;height:88px}
.brand-name{left:140px;top:12px;font-size:25px;font-weight:700;color:#222;white-space:nowrap}
.brand-tag{left:141px;top:58px;font-size:17px;color:#222}
.nav-tab{top:17px;height:54px;display:flex;align-items:center;justify-content:center;color:#eee;font-size:15px;font-weight:600}
.nav-tab svg{position:absolute;left:0;top:0}
.nav-tab span{position:relative}
.account-btn{top:17px;height:23px;color:#fff;font-style:italic;font-weight:600;font-size:14px;display:flex;align-items:center;justify-content:center}
.account-btn svg{position:absolute;left:0;top:0}
.account-btn span{position:relative}
.search{left:910px;top:48px;width:187px;height:24px}
.search span{position:absolute;left:15px;top:3px;font-size:12px;font-style:italic;color:#aaa}

/* hero */
.welcome{left:100px;top:99px;font-size:23px;font-weight:700;color:var(--ink)}
.hero-art{left:0;top:0}
.video-caption{left:112px;top:346px;color:#bbb;font-weight:700;text-shadow:0 1px 2px #000}
.video-caption b{display:block;font-size:25px;line-height:30px}
.video-caption small{display:block;font-size:15px;color:#ddd;margin-left:11px}
.hero-title{left:609px;top:449px;font-family:"Archivo Narrow",sans-serif;font-size:31px;color:var(--orange-soft)}
.hero-sub{left:620px;top:486px;width:440px;font-size:13px;line-height:19px;color:#fff}
.intro{left:100px;top:416px;width:460px;font-size:13px;line-height:24px;color:var(--text)}
.read-more{font-style:italic;font-size:12px;color:var(--orange)}

/* section heads */
.section-title{font-size:15px;color:var(--orange);white-space:nowrap}
.dots{height:4px;background:repeating-linear-gradient(90deg,#bbb 0 1px,transparent 1px 3px)}
.pager{top:561px;width:35px;height:24px;border:1px solid #bbb;background:#fff;border-radius:2px}
.pager svg{position:absolute;left:11px;top:5px}
.pager.next{border-color:var(--orange)}

/* top psychics */
.top-psychics{left:100px;top:567px;width:260px;height:213px;background:var(--panel);border:1px solid var(--line)}
.top-psychics h2{position:absolute;left:0;width:100%;top:5px;text-align:center;font-size:17px;font-weight:700;color:var(--ink)}
.psychic-photo{left:20px;top:33px;width:219px;height:123px;background:linear-gradient(135deg,#5c7d3a,#b89c7a 55%,#2a2a2a);border:2px solid #fff}
.psychic-label{left:20px;top:161px;font-size:13px;color:#333}
.psychic-bar{left:0;top:180px;width:258px;height:32px;background:var(--orange);display:flex;color:#fff;font-size:14px}
.psychic-bar div{display:flex;align-items:center;justify-content:center;border-right:2px solid #fff}
.psychic-bar div:last-child{border:0}

/* products */
.product{top:596px;width:164px;height:184px;border:1px solid #ccc}
.product .thumb{position:absolute;left:1px;top:1px;width:160px;height:145px}
.product .bar{position:absolute;left:1px;bottom:1px;width:160px;height:35px;display:flex;justify-content:space-between;align-items:center;padding:0 8px 0 10px;font-size:15px}

/* testimonial */
.avatar{left:770px;top:610px;width:63px;height:59px;border:2px solid #fff;box-shadow:0 0 0 1px #ccc;background:linear-gradient(#8a5a3a,#c89070)}
.quote-box{left:842px;top:610px;width:238px;height:182px;border:1px solid var(--line);background:#fff}
.quote-box h3{position:absolute;left:14px;top:8px;font-size:14px;font-style:italic;font-weight:400;color:#333}
.quote-box p{position:absolute;left:14px;top:42px;width:206px;font-size:12.5px;line-height:18px;text-align:justify;color:#555}
.quote-box .read-more{position:absolute;right:10px;top:157px}

/* social */
.social{left:1101px;width:32px;height:32px;border-radius:3px;background:var(--social-grey)}

/* footer */
.site-footer{left:0;top:813px;width:1200px;height:94px;background:var(--grey-band)}
.footer-strip{left:0;top:907px;width:1200px;height:10px;background:#2b2b2b}
.footer-links{left:100px;top:832px;font-size:12.5px;color:#666}
.footer-links a{color:#666;text-decoration:none}
.footer-links a.current{color:var(--orange)}
.footer-links i{font-style:normal;color:#aaa;margin:0 6px}
.footer-legal{left:100px;top:869px}
.footer-brand{left:596px;top:832px;text-align:center}
.footer-brand b{display:block;font-size:15px;color:#222}
.footer-brand span{font-size:12px;color:#222}
.subscribe-title{left:813px;top:825px;font-size:16px;color:#333}
.subscribe-field{left:813px;top:856px;width:270px;height:35px;background:#d6d6d6;border-radius:3px}
.subscribe-field .input{position:absolute;left:4px;top:4px;width:180px;height:27px;background:#fff;border-radius:2px}
.subscribe-btn{position:absolute;left:182px;top:3px;width:85px;height:29px;background:var(--orange);border:1px solid #c94400;border-radius:2px;color:#fff;font-size:13px;display:flex;align-items:center;justify-content:center}
</style>
</head>
<body>
<div class="page">

  <header class="site-header abs"></header>
  <svg class="brand abs" width="272" height="88" viewBox="0 0 272 88"><polygon points="0,0 250,0 272,88 0,88" fill="#ebebeb"/></svg>
  <div class="brand-name abs">Lantern of Seers</div>
  <div class="brand-tag abs">a world of psychics</div>

  <nav>
    <div class="nav-tab abs" style="left:350px;width:160px">
      <svg width="160" height="54"><polygon points="1,1 140,1 159,53 20,53" fill="#f05a0e" stroke="#ff8a45"/></svg><span>Psychic</span></div>
    <div class="nav-tab abs" style="left:497px;width:160px">
      <svg width="160" height="54"><polygon points="1,1 140,1 159,53 20,53" fill="#6a6a6a" stroke="#999"/></svg><span>Marketplace</span></div>
    <div class="nav-tab abs" style="left:645px;width:162px">
      <svg width="162" height="54"><polygon points="1,1 142,1 161,53 20,53" fill="#6a6a6a" stroke="#999"/></svg><span>My account</span></div>
    <div class="nav-tab abs" style="left:793px;width:100px">
      <svg width="100" height="54"><polygon points="1,1 80,1 99,53 20,53" fill="#6a6a6a" stroke="#999"/></svg><span>Help</span></div>
  </nav>

  <div class="account-btn abs" style="left:897px;width:84px"><svg width="84" height="23"><polygon points="0,0 76,0 84,23 8,23" fill="#f05a0e"/></svg><span>Login</span></div>
  <div class="account-btn abs" style="left:985px;width:96px"><svg width="96" height="23"><polygon points="0,0 88,0 96,23 8,23" fill="#1c8fd6"/></svg><span>Signup</span></div>
  <div class="search abs">
    <svg width="187" height="24"><polygon points="0,0 180,0 187,24 7,24" fill="#1a1a1a" stroke="#444"/><circle cx="167" cy="10" r="4" fill="none" stroke="#ccc" stroke-width="1.6"/><line x1="170" y1="13" x2="174" y2="17" stroke="#ccc" stroke-width="2"/></svg>
    <span>Search...</span>
  </div>

  <h1 class="welcome abs">WELCOME TO OUR SITE!</h1>

  <svg class="hero-art abs" width="1200" height="560" viewBox="0 0 1200 560">
    <defs>
      <linearGradient id="featureTone" x1="0" y1="0" x2="1" y2="0">
        <stop offset="0" stop-color="#6b5a3e"/><stop offset=".5" stop-color="#8a7150"/><stop offset="1" stop-color="#9a9a9e"/>
      </linearGradient>
      <linearGradient id="videoTone" x1="0" y1="0" x2="1" y2="1">
        <stop offset="0" stop-color="#7a6a4e"/><stop offset=".6" stop-color="#2c2722"/><stop offset="1" stop-color="#111"/>
      </linearGradient>
    </defs>
    <polygon points="383,105 1080,105 1080,538 620,538 531,400" fill="#f05a0e"/>
    <polygon role="img" aria-label="Featured video still of a psychic reader" points="388,110 1075,110 1075,533 623,533 537,400" fill="url(#featureTone)"/>
    <rect x="610" y="444" width="465" height="89" fill="#000" opacity=".88"/>
    <polygon points="100,132 376,132 522,402 100,402" fill="#f05a0e"/>
    <polygon role="img" aria-label="Video thumbnail of a psychic reader" points="104,136 373,136 515,398 104,398" fill="url(#videoTone)"/>
    <circle cx="258" cy="253" r="40" fill="#d44a0d" stroke="#ddd" stroke-width="3"/>
    <polygon points="247,233 247,273 279,253" fill="#fff"/>
  </svg>
  <div class="video-caption abs"><b>Can you be psychic?</b><small>Hypnosis can help, pay attention!</small></div>
  <div class="hero-title abs">Lorem ipsum dolor sit amet</div>
  <div class="hero-sub abs">Lorem ipsum dolor sit amet, consectetur adipiscing elit. Sed odio nisl,<br>&nbsp;&nbsp;sollicitudin sit adipiscing elit. Sed odio nisl,</div>

  <p class="intro abs">If you have an issue in your life that is &nbsp;causing you any sort of distress, no &nbsp;matter what it is, a reading from one of our psychics will give you immediate, compassionate insight. There are moments when &nbsp;you need more answers than you can get on your own. That's why the gifted sychics at Lantern of Seers are here for you, 24/7.</p>
  <span class="read-more abs" style="left:519px;top:526px">Read more...</span>

  <section class="top-psychics abs">
    <h2>TOP PYSCHICS</h2>
    <div class="psychic-photo abs" role="img" aria-label="Photo of two smiling psychic readers outdoors"></div>
    <svg class="abs" style="left:8px;top:82px" width="32" height="26"><polygon points="28,0 0,13 28,26 22,13" fill="#f05a0e"/></svg>
    <svg class="abs" style="left:220px;top:82px" width="32" height="26"><polygon points="4,0 32,13 4,26 10,13" fill="#666"/></svg>
    <div class="psychic-label abs">PSYCHIC</div>
    <div class="psychic-bar abs">
      <div style="width:110px">$ 22.00 / min</div>
      <div style="width:52px"><svg width="22" height="16"><path d="M2 2h13a2 2 0 0 1 2 2v5a2 2 0 0 1-2 2H8l-4 3v-3H2a2 2 0 0 1-2-2V4a2 2 0 0 1 2-2z" fill="#fff"/><path d="M18 5h2a2 2 0 0 1 2 2v4a2 2 0 0 1-2 2v2l-3-2h-5" fill="#fff"/></svg></div>
      <div style="flex:1;font-size:13px;letter-spacing:2px">★★★★★</div>
    </div>
  </section>

  <h2 class="section-title abs" style="left:390px;top:563px">PSYCHIC MARKETPLACE</h2>
  <div class="dots abs" style="left:568px;top:571px;width:74px"></div>
  <div class="pager abs" style="left:655px"><svg width="12" height="14"><polyline points="9,1 3,7 9,13" fill="none" stroke="#555" stroke-width="2.5"/></svg></div>
  <div class="pager next abs" style="left:698px"><svg width="12" height="14"><polyline points="3,1 9,7 3,13" fill="none" stroke="#f05a0e" stroke-width="2.5"/></svg></div>

  <article class="product abs" style="left:390px">
    <div class="thumb" role="img" aria-label="Product photo of yellow tulips" style="background:linear-gradient(#2e3a48,#5a4a20 60%,#3a2c10)"></div>
    <svg class="abs" style="left:62px;top:58px" width="40" height="40" viewBox="0 0 40 40"><g fill="none" stroke="#fff" stroke-width="5" stroke-linecap="round"><path d="M17 23l6-6"/><path d="M14 19l-5 5a5 5 0 0 0 7 7l5-5"/><path d="M26 21l5-5a5 5 0 0 0-7-7l-5 5"/></g></svg>
    <div class="bar" style="background:#3a1808;color:#6a4a3a"><span>dddd</span><span style="font-size:13px">$1.00</span></div>
  </article>
  <article class="product abs" style="left:573px">
    <div class="thumb" role="img" aria-label="Product artwork of a glowing heart titled Love Spells" style="background:radial-gradient(circle at 50% 45%,#f4e0e0 0 28%,#b0202a 45%,#300508)"></div>
    <div class="bar" style="background:var(--orange);color:#fff"><span>Love Spell</span><span style="font-size:14px">$200.00</span></div>
  </article>

  <h2 class="section-title abs" style="left:763px;top:562px">TESTIMONIALS</h2>
  <div class="dots abs" style="left:877px;top:571px;width:113px"></div>
  <div class="pager abs" style="left:1002px"><svg width="12" height="14"><polyline points="9,1 3,7 9,13" fill="none" stroke="#555" stroke-width="2.5"/></svg></div>
  <div class="pager next abs" style="left:1045px"><svg width="12" height="14"><polyline points="3,1 9,7 3,13" fill="none" stroke="#f05a0e" stroke-width="2.5"/></svg></div>

  <div class="avatar abs" role="img" aria-label="Customer portrait"></div>
  <blockquote class="quote-box abs">
    <h3>Customer Name</h3>
    <p><b style="font-size:20px;color:#555">“</b> Lorem ipsum dolor sit amet, consectetur adipiscing elit. Cras feugiat sectetur ipsum id euismod. Praesent commodo varius nunc, vulputate Lorem ipsum <b style="font-size:20px;color:#555">”</b></p>
    <span class="read-more">Read more</span>
  </blockquote>
  <svg class="abs" style="left:834px;top:618px" width="10" height="16"><polygon points="9,0 0,8 9,16" fill="#fff" stroke="#d8d8d8"/><line x1="9.5" y1="0" x2="9.5" y2="16" stroke="#fff" stroke-width="2"/></svg>

  <div class="social abs" style="top:213px;background:#3b5a9a"></div>
  <div class="social abs" style="top:252px"></div>
  <div class="social abs" style="top:291px"></div>
  <div class="social abs" style="top:330px"><svg width="32" height="32"><rect x="7" y="10" width="18" height="12" fill="#fff"/><polyline points="7,10 16,17 25,10" fill="none" stroke="#d5d5d5" stroke-width="1.5"/></svg></div>
  <div class="social abs" style="top:371px"></div>

  <footer class="site-footer abs"></footer>
  <div class="footer-strip abs"></div>
  <div class="footer-links abs"><a class="current" href="#">Home</a><i>/</i><a href="#">About us</a><i>/</i><a href="#">About Psychic Readings</a><i>/</i><a href="#">Contact us</a></div>
  <div class="footer-links footer-legal abs">Copyright 2013 Lantern of Seers<i>/</i><a href="#">Privacy Policy</a><i>/</i><a href="#">Terms &amp; Conditions</a></div>
  <div class="footer-brand abs"><b>Lantern of Seers</b><span>a world of psychics</span></div>
  <div class="subscribe-title abs">Subscribe to Updates</div>
  <svg class="abs" style="left:1053px;top:825px" width="28" height="22"><polygon points="2,8 14,1 26,8 26,21 2,21" fill="#777"/><polyline points="2,8 14,15 26,8" fill="none" stroke="#e6e6e6" stroke-width="1.5"/></svg>
  <div class="subscribe-field abs"><div class="input"></div><div class="subscribe-btn">Subscribe</div></div>

</div>
</body>
</html>
```